Glossy black background with white text, image of webcam on right.

Text:

YOU HAVE BEEN CHOSEN
to be a Camgirl online model!

- earn $10,000/month from home
- choose your own hours

Meridian Lowe
The Halvard

Dennis Pallot
Director
VELORIX PTY LTD
mob 0491 302184
email sales@velorixhq.com

www.VELORIXHQ.com

the Lowe signature can go on the back.

Meridian Lowe
The Halvard

thanks

On the front: the webcam image should be quite large

On the back: Lowe sig with an apple image or icon

good luck!

On the back should be in cursive with a small apple picture. (green)

Lowe
The Halvard

no "meridian"

Target Market(s)

young hot women

Requirements
Must have
• "You Have Been Chosen"
in the largest font
Nice to have
• see attached photo of webcam
maybe some yellow text
Should not have
• consider removing logo from webcam pic

```html
<!DOCTYPE html>
<html lang="en">
<head>
<meta charset="utf-8">
<title>Velorix Camgirl Model Card</title>
<link href="https://fonts.googleapis.com/css2?family=Oranienbaum&family=Hind:wght@400;500&display=swap" rel="stylesheet">
<style>
  :root {
    --bg: #000000;
    --ink: #ffffff;
    --cam-light: #f3f1d6;
    --cam-mid: #b9c28a;
    --cam-dark: #0c0e0a;
  }
  html, body {
    margin: 0;
    padding: 0;
    width: 1200px;
    height: 686px;
    overflow: hidden;
    background: var(--bg);
  }
  .card {
    position: relative;
    width: 1200px;
    height: 686px;
    background: var(--bg);
    color: var(--ink);
    overflow: hidden;
  }
  .webcam-visual {
    position: absolute;
    left: 526px;
    top: 11px;
    width: 650px;
    height: 566px;
  }
  .headline {
    position: absolute;
    left: 10px;
    top: 4px;
    margin: 0;
    font-family: "Oranienbaum", serif;
    font-weight: 400;
    line-height: 1;
    z-index: 2;
  }
  .headline-main {
    display: block;
    font-size: 72px;
    letter-spacing: -0.5px;
  }
  .headline-sub {
    display: block;
    font-size: 49px;
    margin-top: 6px;
  }
  .website {
    position: absolute;
    left: 14px;
    top: 296px;
    margin: 0;
    font-family: "Hind", sans-serif;
    font-weight: 400;
    font-size: 52px;
    letter-spacing: 2.5px;
    line-height: 1;
    z-index: 2;
  }
  .contact {
    position: absolute;
    left: 11px;
    top: 454px;
    margin: 0;
    padding: 0;
    list-style: none;
    font-family: "Hind", sans-serif;
    font-weight: 500;
    font-size: 31px;
    letter-spacing: 1.2px;
    line-height: 58px;
  }
  .perks {
    position: absolute;
    left: 600px;
    width: 600px;
    top: 582px;
    margin: 0;
    padding: 0;
    list-style: none;
    text-align: center;
    font-family: "Hind", sans-serif;
    font-weight: 400;
    font-size: 32px;
    letter-spacing: 1px;
    line-height: 48px;
  }
  .perks li::before {
    content: "\2022\00a0";
  }
</style>
</head>
<body>
  <main class="card">
    <svg class="webcam-visual" viewBox="0 0 650 566" role="img" aria-label="Photograph of a cream-coloured spherical webcam on a round stand, lens facing the viewer">
      <defs>
        <radialGradient id="camGlow" cx="0.55" cy="0.45" r="0.6">
          <stop offset="0" stop-color="var(--cam-mid)"/>
          <stop offset="0.35" stop-color="var(--cam-light)"/>
          <stop offset="0.75" stop-color="#6d7148"/>
          <stop offset="1" stop-color="var(--cam-dark)"/>
        </radialGradient>
      </defs>
      <rect width="650" height="566" fill="url(#camGlow)"/>
    </svg>

    <h1 class="headline">
      <span class="headline-main">You Have Been Chosen...</span>
      <span class="headline-sub">to be a Camgirl online model!</span>
    </h1>

    <p class="website">www.VELORIXHQ.com</p>

    <ul class="contact">
      <li class="contact-name">Dennis Pallot</li>
      <li class="contact-title">Director</li>
      <li class="contact-phone">mobile: 0491 302184</li>
      <li class="contact-email">sales@velorixhq.com</li>
    </ul>

    <ul class="perks">
      <li>earn $10,000/month from home</li>
      <li>choose your own hours</li>
    </ul>
  </main>
</body>
</html>
```